business cards foreign exchange student company
Bluebird Hosting
Bright & Fun-filled
Mack Dorran
Service Director
Western Region
mack@mybluebirdhosting.com
mybluebirdhosting.com
This business card needs to be unforgettable! It needs to stand out from all the other business cards. Something clever/funny. It needs to communicate this is fun!! this is exciting!! and our theme for our company is "The Best Time Ever!" so the business card should convey that they have just found The Best Time Ever!!!
This will be my new website (with the old logo)
this is a marketing piece used to send families to the website
another marketing piece to get families to the website
This is my logo .ai file
This is my .ai logo file for dark backgrounds

```html
<!DOCTYPE html>
<html lang="en">
<head>
<meta charset="utf-8">
<title>Bluebird Hosting – Business Card</title>
<link rel="stylesheet" href="https://fonts.googleapis.com/css2?family=Cormorant+SC:wght@500;600&display=swap">
<style>
  :root {
    --backdrop: #e9e6e1;
    --card: #ffffff;
    --brand-blue: #2a73b8;
    --text-blue: #3a6fa8;
    --icon-blue: #2f6db0;
    --leaf-light: #8fd07a;
    --leaf-dark: #3f9a3a;
  }
  html, body {
    margin: 0;
    width: 1200px;
    height: 900px;
    overflow: hidden;
    background: var(--backdrop);
  }
  .card {
    position: absolute;
    left: 150px;
    top: 193px;
    width: 900px;
    height: 514px;
    background: var(--card);
    box-shadow: 0 10px 30px rgba(0,0,0,0.18);
    font-family: "Cormorant SC", "Times New Roman", serif;
  }
  .brand {
    position: absolute;
    left: 62px;
    top: 72px;
    display: flex;
    align-items: center;
    gap: 14px;
  }
  .brand-dot {
    width: 58px;
    height: 58px;
    border-radius: 50%;
    background: var(--brand-blue);
  }
  .brand-name {
    font-size: 46px;
    font-weight: 600;
    color: var(--brand-blue);
    line-height: 1;
  }
  .tagline {
    position: absolute;
    left: 136px;
    top: 128px;
    font-size: 22px;
    font-weight: 600;
    color: var(--brand-blue);
  }
  .person {
    position: absolute;
    left: 62px;
    top: 232px;
    color: var(--text-blue);
  }
  .person-name {
    margin: 0;
    font-size: 30px;
    font-weight: 600;
    line-height: 1.05;
  }
  .person-role {
    margin: 0;
    font-size: 21px;
    font-weight: 500;
    line-height: 1.1;
  }
  .contact-list {
    list-style: none;
    margin: 22px 0 0;
    padding: 0;
    font-size: 19px;
    font-weight: 500;
    line-height: 26px;
  }
  .contact-list li {
    display: flex;
    align-items: center;
    gap: 10px;
  }
  .contact-icon {
    width: 14px;
    height: 14px;
    flex: none;
  }
  .emblem {
    position: absolute;
    left: 560px;
    top: 40px;
    width: 300px;
    height: 380px;
  }
</style>
</head>
<body>
  <div class="card">
    <div class="brand">
      <span class="brand-dot"></span>
      <span class="brand-name">Bluebird Hosting</span>
    </div>
    <div class="tagline">Bright &amp; Fun-filled</div>

    <div class="person">
      <p class="person-name">Mack Dorran</p>
      <p class="person-role">Service Director</p>
      <ul class="contact-list">
        <li><svg class="contact-icon" viewBox="0 0 14 14"><circle cx="7" cy="7" r="7" fill="var(--icon-blue)"/><path d="M7 3.2a2.4 2.4 0 0 0-2.4 2.4c0 1.8 2.4 4.6 2.4 4.6s2.4-2.8 2.4-4.6A2.4 2.4 0 0 0 7 3.2z" fill="#fff"/></svg>Western Region</li>
        <li><svg class="contact-icon" viewBox="0 0 14 14"><circle cx="7" cy="7" r="7" fill="var(--icon-blue)"/><path d="M4.6 3.8l1.4-.3.8 2-1 .7a5 5 0 0 0 2 2l.7-1 2 .8-.3 1.4c-3 .3-5.9-2.6-5.6-5.6z" fill="#fff"/></svg>8775550142</li>
        <li><svg class="contact-icon" viewBox="0 0 14 14"><circle cx="7" cy="7" r="7" fill="var(--icon-blue)"/><rect x="4.6" y="3" width="4.8" height="8" rx="0.8" fill="#fff"/></svg>8015550187</li>
        <li><svg class="contact-icon" viewBox="0 0 14 14"><circle cx="7" cy="7" r="7" fill="var(--icon-blue)"/><rect x="3.5" y="4.5" width="7" height="5" fill="#fff"/></svg>18015550163</li>
        <li><svg class="contact-icon" viewBox="0 0 14 14"><circle cx="7" cy="7" r="7" fill="var(--icon-blue)"/><path d="M3.5 4.5h7v5h-7z M3.5 4.5 7 7.3l3.5-2.8" fill="#fff" stroke="var(--icon-blue)" stroke-width="0.6"/></svg>mack@mybluebirdhosting.com</li>
        <li><svg class="contact-icon" viewBox="0 0 14 14"><circle cx="7" cy="7" r="7" fill="var(--icon-blue)"/><circle cx="7" cy="7" r="3.6" fill="none" stroke="#fff" stroke-width="1"/><path d="M3.4 7h7.2M7 3.4v7.2" stroke="#fff" stroke-width="0.8"/></svg>www.mybluebirdhosting.com</li>
      </ul>
    </div>

    <svg class="emblem" role="img" aria-label="Large brand emblem decoration in green" viewBox="0 0 300 380">
      <defs>
        <radialGradient id="emblem-fill" cx="40%" cy="35%" r="70%">
          <stop offset="0%" stop-color="var(--leaf-light)"/>
          <stop offset="100%" stop-color="var(--leaf-dark)"/>
        </radialGradient>
      </defs>
      <circle cx="150" cy="190" r="140" fill="url(#emblem-fill)"/>
    </svg>
  </div>
</body>
</html>
```